Trade Show Banner

Looking for a design for 36" x 90" stretched fabric display.
Commercial construction company, can include Chicago high rise buildings, blue prints, steel studs.
List of types of work should include:
Commercial office build-out
Hospital expansion
Educational and institutional
Laboratory and research
Dental and medical office
Veterinary Clinics

website brolmerconstruction.com

Target Market(s)

Architects and General Contractors

Industry/Entity Type

Commercial Construction

Colors
0054AA
0677BA
7BADD7
CADEEF
E8F1F8

Requirements
Must have
• Our logo, blueprints, chicago high rise
Should not have
• no cartoon construction logos, no houses

```html
<!DOCTYPE html>
<html lang="en">
<head>
<meta charset="utf-8">
<title>Brolmer Construction – Trade Show Banner</title>
<link rel="stylesheet" href="https://fonts.googleapis.com/css2?family=Exo+2:ital,wght@0,400;0,500;0,800;1,900&display=swap">
<style>
  :root {
    --blue: #0054aa;
    --blue-mid: #0677ba;
    --blue-light: #7badd7;
    --blue-pale: #cadeef;
    --ice: #e8f1f8;
    --charcoal: #464646;
    --ink: #3d3d3d;
    --page: #d4d6d8;
    --white: #ffffff;
  }
  * { box-sizing: border-box; margin: 0; padding: 0; }
  html, body { width: 1200px; height: 1191px; overflow: hidden; background: var(--page); }
  body { position: relative; font-family: "Exo 2", sans-serif; }

  .banner {
    position: absolute; left: 30px; top: 367px;
    width: 1140px; height: 456px;
    background: var(--white); overflow: hidden;
  }
  .banner-art { position: absolute; inset: 0; width: 100%; height: 100%; }

  .brand {
    position: absolute; left: 619px; top: 40px;
    display: flex; align-items: center; gap: 18px;
  }
  .brand-mark { width: 64px; height: 64px; background: var(--blue); }
  .brand-name {
    font-weight: 800; font-size: 40px; line-height: 1;
    color: var(--blue); text-transform: uppercase; letter-spacing: 1px;
  }

  .headline {
    position: absolute; left: 590px; width: 470px; top: 146px;
    text-align: center; font-weight: 900; font-style: italic;
    font-size: 33px; line-height: 34px; color: var(--ink); text-transform: uppercase;
  }
  .headline .accent { color: var(--blue); display: block; }

  .rule { position: absolute; left: 537px; width: 571px; height: 2px; background: var(--blue); }
  .rule.top { top: 261px; }
  .rule.bottom { top: 357px; }

  .services {
    position: absolute; top: 271px; list-style: none;
    font-size: 20.5px; line-height: 25px; color: var(--ink); font-weight: 400;
  }
  .services.left { left: 537px; }
  .services.right { left: 851px; }
  .services li { display: flex; align-items: center; gap: 6px; white-space: nowrap; }
  .tick { width: 15px; height: 15px; flex: none; }
  .col-divider { position: absolute; left: 836px; top: 274px; width: 1.5px; height: 74px; background: var(--ink); }

  .web {
    position: absolute; left: 508px; top: 388px; width: 600px;
    text-align: center; color: var(--white); font-weight: 500;
    font-size: 44px; line-height: 48px; letter-spacing: 0.5px;
  }
</style>
</head>
<body>
  <section class="banner">
    <svg class="banner-art" viewBox="0 0 1815 726" preserveAspectRatio="none" aria-hidden="false">
      <defs>
        <linearGradient id="sky" x1="0" y1="0" x2="0" y2="1">
          <stop offset="0" stop-color="#3f8fd6"/><stop offset="1" stop-color="#a9cbe6"/>
        </linearGradient>
        <linearGradient id="paper" x1="0" y1="0" x2="1" y2="1">
          <stop offset="0" stop-color="#f4f4f2"/><stop offset="1" stop-color="#d9d9d6"/>
        </linearGradient>
        <linearGradient id="scaffold" x1="0" y1="0" x2="1" y2="1">
          <stop offset="0" stop-color="#8fc3ea"/><stop offset="0.55" stop-color="#b89a52"/><stop offset="1" stop-color="#6e5a2e"/>
        </linearGradient>
        <linearGradient id="towers" x1="0" y1="0" x2="0" y2="1">
          <stop offset="0" stop-color="#5e9ad6"/><stop offset="1" stop-color="#233f70"/>
        </linearGradient>
      </defs>
      <polygon fill="url(#sky)" points="0,0 532,0 365,480 0,385" role="img" aria-label="Photo: Chicago high-rise tower between city buildings"/>
      <polygon fill="url(#paper)" points="0,395 360,490 290,726 0,726" role="img" aria-label="Photo: hands unrolling architectural blueprints"/>
      <polygon fill="url(#towers)" points="545,0 930,0 838,272 500,178" role="img" aria-label="Photo: glass skyscrapers against the sky"/>
      <polygon fill="url(#scaffold)" points="495,190 822,282 722,660 372,558" role="img" aria-label="Photo: scaffolding on a building under construction"/>
      <polygon fill="var(--charcoal)" points="372,570 690,660 670,726 300,726"/>
      <polygon fill="var(--charcoal)" points="918,0 936,0 738,680 720,680"/>
      <polygon fill="var(--charcoal)" points="752,605 1767,605 1767,700 722,700"/>
    </svg>

    <svg width="0" height="0" style="position:absolute">
      <symbol id="tick" viewBox="0 0 16 16">
        <circle cx="8" cy="8" r="8" fill="var(--blue)"/>
        <path d="M4.3 8.3l2.4 2.4 5-5" fill="none" stroke="#fff" stroke-width="2.2" stroke-linecap="round" stroke-linejoin="round"/>
      </symbol>
    </svg>

    <div class="brand">
      <span class="brand-mark"></span>
      <span class="brand-name">Brolmer Construction</span>
    </div>

    <h1 class="headline">We are the part<br>of the ever changing<span class="accent">Chicago skyline</span></h1>

    <div class="rule top"></div>
    <ul class="services left">
      <li><svg class="tick"><use href="#tick"/></svg>Commercial office build-out</li>
      <li><svg class="tick"><use href="#tick"/></svg>Hospital expansion</li>
      <li><svg class="tick"><use href="#tick"/></svg>Educational and institutional</li>
    </ul>
    <div class="col-divider"></div>
    <ul class="services right">
      <li><svg class="tick"><use href="#tick"/></svg>Laboratory and research</li>
      <li><svg class="tick"><use href="#tick"/></svg>Dental and medical office</li>
      <li><svg class="tick"><use href="#tick"/></svg>Veterinary Clinics</li>
    </ul>
    <div class="rule bottom"></div>

    <p class="web">brolmerconstruction.com</p>
  </section>
</body>
</html>
```